Letterhead for financial advisor-insurance agent firm

Our company, Harlow Pemberton Insurance & Investments, is an insurance (health, life, home, auto, etc) and investment brokerage offering a suite of options to meet client needs. We need letterhead that is professional and embodies strength, security and sophistication.

http://jobs.brieftrove.example/job.aspx?id=518264

Industry/Entity Type

Investment

```html
<!DOCTYPE html>
<html lang="en">
<head>
<meta charset="utf-8">
<title>Harlow Pemberton Insurance &amp; Investments — Letterhead</title>
<link rel="stylesheet" href="https://fonts.googleapis.com/css2?family=Cinzel:wght@400&display=swap">
<style>
  :root {
    --paper: #ffffff;
    --ink-navy: #343f52;
    --frame: #1a1a1a;
    --accent-grey: #d3d6da;
  }
  html, body {
    margin: 0;
    padding: 0;
    overflow: hidden;
    background: var(--paper);
  }
  .letterhead {
    position: relative;
    width: 859px;
    height: 1200px;
    background: var(--paper);
    overflow: hidden;
  }
  .page-frame {
    position: absolute;
    left: 14px;
    top: 11px;
    width: 832px;
    height: 1179px;
    border: 1px solid var(--frame);
    box-sizing: border-box;
    pointer-events: none;
  }
  .corner-accent {
    position: absolute;
    left: 15px;
    top: 640px;
    width: 830px;
    height: 549px;
    background:
      linear-gradient(35deg, var(--accent-grey) 0%, rgba(220, 223, 227, 0.75) 35%, rgba(255, 255, 255, 0) 75%);
    -webkit-mask-image: linear-gradient(to right, transparent 0%, #000 45%);
    mask-image: linear-gradient(to right, transparent 0%, #000 45%);
  }
  .brand {
    position: absolute;
    top: 91px;
    left: 0;
    width: 859px;
    display: flex;
    flex-direction: column;
    align-items: center;
    font-family: "Cinzel", "Times New Roman", serif;
    font-weight: 400;
    color: var(--ink-navy);
  }
  .brand__square {
    width: 56px;
    height: 56px;
    border: 2px solid var(--ink-navy);
    box-sizing: border-box;
  }
  .brand__name {
    margin: 10px 0 0;
    font-size: 20px;
    font-weight: 400;
    line-height: 1;
    letter-spacing: 0;
  }
  .brand__tagline {
    margin: 4px 0 0;
    font-size: 9.5px;
    line-height: 1;
    letter-spacing: 0.04em;
  }
</style>
</head>
<body>
  <main class="letterhead">
    <div class="corner-accent" role="img" aria-label="Soft grey decorative accent in the lower right corner"></div>
    <div class="page-frame"></div>

    <header class="brand">
      <div class="brand__square"></div>
      <h1 class="brand__name">Harlow Pemberton</h1>
      <p class="brand__tagline">Insurance &amp; Investments</p>
    </header>
  </main>
</body>
</html>
```